Design a label for a dog shampoo names furbloom, the sell point of this series of shampoo is “just like wash your dogs with milk, not harm for your hand ”, the style could be gentle or professional or even amazing.

Use only 2 colors in the design job, the color of our logo could be changed, it depends on your whole page. Please design in CDR or ai.

update:
Pls do more change with the fonts when you design the front page, including title and details. Try more styles of fonts. Addition, this design will be printed on the bottle, no a label stick on it.
Updates

Do not put a real dog or animal on the page, Pay more attention to the types of fonts

Reason: Expect for more design idea.

Target Market(s)

people 20-30 years old who have dogs and cats at home

Industry/Entity Type

It Professional

Requirements
Nice to have
• It would be nice if you add some detail words in the design of the right side.

```html
<!DOCTYPE html>
<html lang="en">
<head>
<meta charset="utf-8">
<title>furbloom Super-conditioning &amp; Nutrient Shampoo – Bottle Print</title>
<link rel="stylesheet" href="https://fonts.googleapis.com/css2?family=Quicksand:wght@400;500;700&family=PT+Sans+Narrow:wght@400;700&display=swap">
<style>
  :root {
    --cyan: #6fcedd;
    --cyan-deep: #1ebcd5;
    --cyan-text: #20b2c9;
    --teal: #17998b;
    --teal-text: #12808f;
    --white: #ffffff;
    --stage: #8a8a8a;
  }
  * { box-sizing: border-box; margin: 0; padding: 0; }
  html, body { width: 1200px; height: 1000px; overflow: hidden; }
  body {
    background: var(--stage);
    position: relative;
    font-family: "PT Sans Narrow", "Arial Narrow", sans-serif;
  }
  .label {
    position: absolute;
    background: var(--cyan);
    border-radius: 26px;
    box-shadow: 0 6px 18px rgba(0,0,0,.3);
  }
  .label-back { left: 120px; top: 75px; width: 442px; height: 853px; }
  .label-front { left: 637px; top: 75px; width: 446px; height: 847px; }
  .stitch { position: absolute; inset: 0; width: 100%; height: 100%; }
  .panel {
    position: absolute; inset: 18px 17px;
    border-radius: 12px; overflow: hidden;
    background: var(--white);
  }
  .label-back .panel { background: linear-gradient(180deg, #a6e1ea 0, #d8f2f6 200px, #fff 230px); }
  .label-front .panel { background: linear-gradient(180deg, var(--cyan-deep) 0, #8fd9e6 300px, #e6f7fa 520px, #fff 800px); }

  .brand-name {
    position: absolute;
    font-family: "Quicksand", sans-serif;
    font-weight: 700;
    color: var(--teal);
    white-space: nowrap;
  }
  .tagline {
    position: absolute;
    font-family: "Quicksand", sans-serif;
    font-weight: 500;
    color: var(--white);
    line-height: 1.2;
    white-space: nowrap;
  }
  .title-band {
    position: absolute;
    background: var(--teal);
    color: var(--white);
    font-family: "Quicksand", sans-serif;
    font-weight: 500;
    line-height: 1.15;
    white-space: nowrap;
  }

  /* back */
  .label-back .brand-name { left: 24px; top: 42px; font-size: 30px; }
  .label-back .tagline { left: 180px; top: 28px; font-size: 17px; }
  .label-back .title-band { left: 14px; top: 97px; width: 376px; height: 100px; padding: 14px 0 0 26px; font-size: 31px; }
  .copy {
    position: absolute; left: 19px; top: 213px; width: 372px;
    font-size: 14.2px; line-height: 1.14; color: var(--teal-text);
    text-align: justify;
  }
  .copy strong { font-weight: 700; }
  .copy .head { color: var(--cyan-text); font-size: 15px; font-weight: 700; }
  .copy .block { margin-top: 13px; }
  .copy ul { list-style: none; width: 300px; text-align: left; margin-top: 2px; }
  .copy li { padding-left: 14px; position: relative; }
  .copy li::before { content: "•"; position: absolute; left: 0; }
  .bubbles-small { position: absolute; left: 315px; top: 335px; width: 90px; height: 170px; border-radius: 45px;
    background: radial-gradient(circle at 40% 40%, rgba(150,220,235,.7), rgba(150,220,235,0) 70%); }
  .contact { position: absolute; left: 16px; top: 728px; width: 195px; font-size: 14.5px; line-height: 1.1; color: var(--teal-text); }

  /* front */
  .label-front .tagline { left: 0; width: 412px; top: 26px; font-size: 28px; text-align: center; }
  .label-front .brand-name { left: 0; width: 412px; top: 200px; font-size: 64px; text-align: center; }
  .label-front .title-band { left: 14px; top: 324px; width: 386px; height: 150px; padding: 36px 0 0 22px; font-size: 35px; }
  .bubbles-large { position: absolute; left: 20px; top: 485px; width: 372px; height: 320px; border-radius: 40px;
    background: radial-gradient(ellipse at 50% 45%, rgba(140,215,232,.75), rgba(200,238,245,.2) 75%); }
  .claims { position: absolute; left: 0; width: 412px; top: 725px; text-align: center; color: var(--teal); font-size: 19px; line-height: 1.05; }
  .volume { display: block; font-size: 9px; margin-top: 14px; }
</style>
</head>
<body>

<section class="label label-back">
  <svg class="stitch" viewBox="0 0 442 853" aria-hidden="true"><rect x="8" y="8" width="426" height="837" rx="20" fill="none" stroke="#fff" stroke-width="6" stroke-dasharray="12 7" stroke-linecap="round"/></svg>
  <div class="panel">
    <div class="brand-name">furbloom</div>
    <p class="tagline">As gentle as milk for your<br>dog’s coat and your hands</p>
    <h2 class="title-band">Super-conditioning<br>&amp; Nutrient Shampoo</h2>
    <div class="bubbles-small" role="img" aria-label="Soft floating bubbles decoration"></div>
    <div class="copy">
      <p><strong>FURBLOOM Super-Conditioning &amp; Nutrient Shampoo</strong> is a specially formulated shampoo, rich in conditioners derived from milk which easily penetrates and nourishes your pet’s coat from root to tip. With the help of negative ions, excess shampoo rinses out quickly and completely to leave a soft, sparkling, and smooth coat. Safe and gentle enough to be used every day. Safe for even the most sensitive skins and coats of puppies, lactating bitches and cats</p>
      <div class="block"><span class="head">DIRECTIONS</span>
        <ul>
          <li>Before shampooing, brush out pet’s coat.</li>
          <li>Saturate dog’s coat with lukewarm water.</li>
          <li>Dispense a small amount of shampoo into the palm of your hand.</li>
          <li>To clean coat, start at dog’s head and work back towards the tail. Avoid getting shampoo into the dog’s eyes and ears.</li>
          <li>Rinse coat several times with lukewarm water.</li>
          <li>Towel dry and gently comb or brush coat.</li>
        </ul>
      </div>
      <p class="block"><span class="head">ACTIVE INGREDIENTS</span> Hypochlorous Acid, Sodium Hypochlorite</p>
      <p class="block"><span class="head">SAFETY PRECAUTIONS</span> Harmful if swallowed.<br>Do not inhale. Discontinue use if irritation develops and contact your veterinarian. For animal use only. Not for human use. Keep out of reach of children. Do not decant into smaller containers. Not for injection. Always consult with a Veterinarian for systemic conditions.</p>
      <p class="block"><span class="head">STORAGE AND DISPOSAL</span> Keep out of the reach of children.<br>Replace Cap. Wrap in several layers of newspaper and discard in trash.</p>
    </div>
    <p class="contact">Contact details etc Contact details etc Contact details etc Contact details etc Contact details etc</p>
  </div>
</section>

<section class="label label-front">
  <svg class="stitch" viewBox="0 0 446 847" aria-hidden="true"><rect x="8" y="8" width="430" height="831" rx="20" fill="none" stroke="#fff" stroke-width="6" stroke-dasharray="12 7" stroke-linecap="round"/></svg>
  <div class="panel">
    <p class="tagline">As gentle as milk for your<br>dog’s coat and your hands</p>
    <div class="brand-name">furbloom</div>
    <h1 class="title-band">Super-conditioning<br>&amp; Nutrient Shampoo</h1>
    <div class="bubbles-large" role="img" aria-label="Cluster of soft translucent bubbles"></div>
    <p class="claims">MOISTURE-RICH<br>SMOOTH AND SILKY<span class="volume">1000 ML</span></p>
  </div>
</section>

</body>
</html>
```